MARLOWE BRIGHT WORKS WEBSITE HOME PAGE AND CHECKOUT PAGES

UPDATE TO BRIEF:

Marlowe Bright Works is a company that provides Charities with the Free Vacation Vouchers that they can use to incentivize people to donate which in turn increases donations for the chairty.

So I need to keep it a little more template like the example url I gave. http://pagefernly.com/marlowe-bright-work/ Because, I am going to provide template to ANY CHARITY TYPE and they just fill in the content into the template and change images or whatever for their charity. So I am really looking for a website template that can be used for multiple and different kinds of charities.

So where the logo would go please use YOUR LOGO HERE generic logo for now

and where ever you promote the Free Vacation Certificate To Las Vegas please add "Brought To You By" (logo marlowe bright works or something...basically its a partnership with the Charity and Marlowe Bright Work)

So Marlowe Bright Work is a marketing company and not a Charity but more of a plug and play platform that allows a charity to accepts donations and immediately deliver the promised incentive offer after donation is made on the website.

When a Charity is able to offer a high perceived value gift for a donation they increase donations.

Target Market(s)

PEOPLE THAT DONATE TO CHARITIES

Industry/Entity Type

Charity

Number of Pages Required

3 page

Requirements
Must have
• One thing i need to add to the website is an Incentive Gift for the Donation.

So I need this tagline and images to make the promotion seem great:
"Donate $100 and Receive A Free 3 Night Vacation Certificate To Las Vegas!"

Maybe show image of vegas or some kind of nice graphic that promotes the vegas vacation as a gift for the $100 donation very well"

I need the payment pages as well. So when someone click Donate Now, the next page is there where they can see their gift that is included with the donation, and also the donation amount...
Nice to have

Should not have

```html
<!DOCTYPE html>
<html lang="en">
<head>
<meta charset="utf-8">
<title>Marlowe Bright Works – Home</title>
<link href="https://fonts.googleapis.com/css2?family=Lato:wght@400;700;900&display=swap" rel="stylesheet">
<style>
:root{
  --orange:#f26a10;
  --blue:#22b5e2;
  --ink:#1f2126;
  --text:#333;
  --muted:#555;
  --ice:#e4f6fc;
  --grey:#f2f2f2;
  --white:#fff;
}
*{box-sizing:border-box;margin:0;padding:0}
html,body{width:1200px;height:4914px;overflow:hidden}
body{position:relative;font-family:'Lato',sans-serif;color:var(--text);background:var(--white)}
.abs{position:absolute}
.center{text-align:center}
.btn-pill{position:absolute;display:flex;align-items:center;gap:12px;background:var(--orange);color:var(--white);font-weight:900;font-size:15px;border-radius:24px;padding:0 22px 0 6px;height:40px;text-transform:uppercase;border:3px solid rgba(255,255,255,.85)}
.btn-pill .heart{width:28px;height:28px;border-radius:50%;background:var(--white);display:flex;align-items:center;justify-content:center}
.brand-name{font-weight:900;font-size:30px;color:var(--blue);display:flex;align-items:center;gap:10px}
.brand-name .dot{width:22px;height:22px;border-radius:50%;background:var(--blue)}

/* header */
.site-header{top:0;left:0;width:1200px;height:84px;background:var(--white)}
.menu-icon{left:145px;top:31px;width:22px;height:18px}
.menu-icon span{display:block;height:3px;background:var(--ink);margin-bottom:4px}

/* hero */
.hero{top:84px;left:0;width:1200px;height:628px;background:linear-gradient(180deg,#6f87b6 0%,#a9bbd9 35%,#e9eef6 70%,#f5f7fb 100%)}
.hero-kicker{top:302px;width:1200px;font-weight:700;font-size:22px;color:#1d2230}
.hero-title{top:338px;width:1200px;font-weight:900;font-size:50px;line-height:48px;color:#141821}
.dots{top:577px;left:564px;display:flex;gap:8px}
.dots span{width:18px;height:18px;border-radius:50%;border:2px solid #333}
.dots span.on{background:var(--orange);border-color:#333}

/* promo band */
.promo{top:712px;left:0;width:1200px;height:179px}
.promo-copy{color:var(--white);font-size:16px;font-weight:700;line-height:20px}
.promo-copy a{display:block;margin-top:10px;color:var(--white);text-decoration:underline;font-size:15px}
.promo-icon{width:68px;height:68px;border-radius:50%;display:flex;align-items:center;justify-content:center}

/* habitat columns */
.col-title{font-weight:900;font-size:18px;color:var(--ink);text-transform:uppercase;line-height:24px}
.col-text{font-size:13.5px;line-height:21px;color:var(--muted)}
.ring{border-radius:50%;border:4px solid var(--blue);padding:6px;background:var(--white)}
.ring div{width:100%;height:100%;border-radius:50%}

/* quote */
.quote{top:1542px;left:0;width:1200px;height:503px;background:linear-gradient(135deg,#3a3c42 0%,#25272c 55%,#17181b 100%)}
.quote-line{width:1200px;font-weight:900;font-size:37px;line-height:47px;color:var(--orange)}
.quote-by{width:1200px;font-weight:700;font-size:18px;color:var(--white)}

/* arctic */
.arctic{top:2045px;left:0;width:1200px;height:598px;background:linear-gradient(180deg,#22b5e2 0%,#2cbbe5 60%,#3ec3ea 100%)}
.arctic h2{font-weight:900;font-size:40px;line-height:48px;color:var(--white)}
.rule{height:4px;background:var(--white)}
.arctic p{font-size:15px;line-height:23px;color:#e9f8fd}
.btn-box{position:absolute;background:var(--orange);color:var(--white);font-weight:900;font-size:15px;display:flex;align-items:center;justify-content:center;text-transform:uppercase}

/* features */
.feature{width:282px;height:328px;color:var(--white);padding:0 18px}
.feature h3{margin-top:90px;font-weight:900;font-size:16px;line-height:20px;text-transform:uppercase}
.feature p{margin-top:12px;font-size:13.5px;line-height:21px}
.feature-icon{width:68px;height:68px;background:var(--white)}

/* news */
.news{top:3177px;left:0;width:1200px;height:853px;background:linear-gradient(180deg,#3b3d43 0%,#26282d 50%,#1b1c20 100%)}
.news h2{width:1200px;font-weight:900;font-size:42px;color:var(--white)}
.card{width:286px;height:393px;background:var(--white);box-shadow:0 4px 12px rgba(0,0,0,.3)}
.card .photo{height:183px;position:relative}
.card .date{position:absolute;left:10px;top:0;background:#c45a10;color:var(--white);font-weight:900;font-size:13px;line-height:15px;padding:4px 8px;text-align:center}
.card h4{margin-top:22px;font-weight:900;font-size:15px;line-height:20px;text-transform:uppercase;color:var(--ink)}
.card p{margin:10px 20px 0;font-size:13px;line-height:20px;color:var(--muted)}
.card .more{margin:14px auto 0;width:126px;height:38px;border:2px solid var(--ink);font-weight:900;font-size:14px;display:flex;align-items:center;justify-content:center;color:var(--ink)}

/* gift cta */
.gift{top:4030px;left:0;width:1200px;height:416px;background:var(--grey)}
.gift h2{width:1200px;font-weight:900;font-size:38px;line-height:48px;color:var(--orange)}
.gift p{width:1200px;font-size:17px;color:var(--ink)}

/* footer */
.footer{top:4446px;left:0;width:1200px;height:468px;background:#24262b;color:#d8d8d8}
.footer h5{font-weight:900;font-size:17px;color:var(--white);text-transform:uppercase}
.foot-item{display:flex;gap:18px;font-size:14px;line-height:21px}
.foot-item svg{flex:none;margin-top:2px}
.email-field{width:304px;height:38px;background:var(--white);border:1px solid #ccc;font-size:13px;color:#777;padding:11px 14px}
.quick a{display:block;color:#d8d8d8;text-decoration:none;font-size:14px;line-height:24px}
.copyright{top:4850px;width:1200px;font-size:13px;color:#d8d8d8}
</style>
</head>
<body>

<header class="abs site-header">
  <div class="abs menu-icon"><span></span><span></span><span></span></div>
  <div class="abs brand-name" style="left:470px;top:24px"><span class="dot"></span>Marlowe Bright Works</div>
  <div class="btn-pill" style="left:902px;top:21px;height:40px;font-size:13px">
    <span class="heart"><svg width="14" height="13" viewBox="0 0 24 22"><path d="M12 21 2 11A6 6 0 0 1 12 3a6 6 0 0 1 10 8Z" fill="#f26a10"/></svg></span>Donate Now
  </div>
</header>

<section class="abs hero" role="img" aria-label="Photo of a polar bear walking across snow under a blue sky"></section>
<div class="abs hero-kicker center">THE POLAR BEARS ESSENTIAL HABITAT.</div>
<h1 class="abs hero-title center">HELP PRESERVE<br>ESSENTIAL POLAR HABITAT.</h1>
<div class="btn-pill" style="left:516px;top:533px">
  <span class="heart"><svg width="14" height="13" viewBox="0 0 24 22"><path d="M12 21 2 11A6 6 0 0 1 12 3a6 6 0 0 1 10 8Z" fill="#f26a10"/></svg></span>Donate Now
</div>
<div class="abs dots"><span class="on"></span><span></span><span></span></div>

<section class="abs promo">
  <svg class="abs" style="left:0;top:0" width="1200" height="179">
    <rect width="1200" height="179" fill="#22b5e2"/>
    <polygon points="0,0 640,0 580,179 0,179" fill="#f26a10"/>
    <path d="M650 8 L588 170" stroke="#fff" stroke-width="4"/>
    <path d="M652 14 l14 -8 -6 14 z" fill="#fff"/>
  </svg>
  <div class="abs promo-icon" style="left:58px;top:55px;background:var(--blue)">
    <svg width="30" height="28" viewBox="0 0 30 28"><rect x="2" y="10" width="26" height="16" fill="#fff"/><rect x="0" y="6" width="30" height="6" fill="#fff"/><rect x="13" y="6" width="4" height="20" fill="#22b5e2"/><path d="M15 6c-4-6-10-5-8-1M15 6c4-6 10-5 8-1" stroke="#fff" stroke-width="2.5" fill="none"/></svg>
  </div>
  <div class="abs promo-copy" style="left:147px;top:54px;width:420px">Donate $100 and Receive A Free 3 Night Vacation Certificate To Las Vegas!"<a>Incentive Gift for the Donation</a></div>
  <div class="abs promo-icon" style="left:674px;top:55px;background:var(--orange)">
    <svg width="30" height="28" viewBox="0 0 30 28"><path d="M15 2 1 14h4v12h8v-8h4v8h8V14h4Z" fill="#fff"/></svg>
  </div>
  <div class="abs promo-copy" style="left:763px;top:54px;width:400px">Donate today &amp; help us reach our $1M goal to preserve the polar bear's Arctic home.<a>Incentive Gift for the Donation</a></div>
</section>

<!-- habitat columns -->
<div class="abs" style="left:439px;top:985px;width:324px;height:459px;background:var(--ice)"></div>

<div class="abs center" style="left:133px;top:1014px;width:270px">
  <div class="col-title">The Polar Bear</div>
  <p class="col-text" style="margin-top:12px">Lorem ipsum dolor sit amet, consctetur adipisicing elit, sed do eiusmod tempor incididunt ut labore et dolore magna aliqua. Ut enim ad minim veniam. Duis aute irure dolor in</p>
</div>
<div class="abs ring" style="left:153px;top:1176px;width:228px;height:228px"><div role="img" aria-label="Photo of a polar bear in warm evening light" style="background:radial-gradient(circle at 50% 45%,#e8dcc8,#a38a6a 70%,#6b5a48)"></div></div>

<div class="abs ring" style="left:487px;top:1019px;width:228px;height:228px"><div role="img" aria-label="Photo of a polar bear on a small ice floe in open water" style="background:linear-gradient(180deg,#b8c6d6 0%,#8fa2b8 50%,#4e6278 100%)"></div></div>
<div class="abs center" style="left:466px;top:1274px;width:270px">
  <div class="col-title">Climate Change</div>
  <p class="col-text" style="margin-top:12px">Lorem ipsum dolor sit amet, consctetur adipisicing elit, sed do eiusmod tempor incididunt ut labore et dolore magna aliqua. Ut enim ad minim veniam. Duis aute irure dolor in</p>
</div>

<div class="abs center" style="left:794px;top:995px;width:270px">
  <div class="col-title">Time Is Running Out For<br>The Polar Bear</div>
  <p class="col-text" style="margin-top:12px">Lorem ipsum dolor sit amet, consctetur adipisicing elit, sed do eiusmod tempor incididunt ut labore et dolore magna aliqua. Ut enim ad minim veniam. Duis aute irure dolor in</p>
</div>
<div class="abs ring" style="left:815px;top:1176px;width:228px;height:228px"><div role="img" aria-label="Photo of a polar bear silhouetted against a red sunset" style="background:radial-gradient(circle at 50% 30%,#e0652a,#9a2a12 55%,#2a0b06)"></div></div>

<!-- quote -->
<section class="abs quote" role="img" aria-label="Dark-toned photo of hands typing on a laptop showing a donate button">
  <svg class="abs" style="left:0;top:0" width="1200" height="90"><path d="M0 0H1200V80Q600 -75 0 80Z" fill="#fff"/></svg>
</section>
<div class="abs quote-line center" style="top:1705px">I Predict That We Could See Ice-Free<br>Summers on the North Pole Within a Decade.</div>
<div class="abs quote-by center" style="top:1810px">Elias Brandt, Lead Researcher, The Northern Ice Research Council</div>
<div class="btn-pill" style="left:516px;top:1865px">
  <span class="heart"><svg width="14" height="13" viewBox="0 0 24 22"><path d="M12 21 2 11A6 6 0 0 1 12 3a6 6 0 0 1 10 8Z" fill="#f26a10"/></svg></span>Donate Now
</div>

<!-- arctic -->
<section class="abs arctic">
  <h2 class="abs" style="left:139px;top:130px">HELP US PROTECT<br>THE ARCTIC</h2>
  <div class="abs rule" style="left:141px;top:246px;width:62px"></div>
  <p class="abs" style="left:141px;top:270px;width:330px">Lorem ipsum dolor sit amet, consectetur aelit, sed do eiusmod tempor incididunt ut labore et dolore magna aliqua. Ut enim ad minim niam, quis nostrud exercitation ullamco laboris</p>
  <div class="btn-box" style="left:141px;top:382px;width:141px;height:40px">Read More</div>
  <div class="abs" role="img" aria-label="Video still of the Arctic seen from space" style="left:574px;top:130px;width:481px;height:317px;background:radial-gradient(ellipse at 45% 55%,#dfe6ec 0%,#8fa0b0 45%,#1a2430 80%,#05080c 100%)"></div>
  <svg class="abs" style="left:791px;top:264px" width="48" height="48"><circle cx="24" cy="24" r="21" fill="#fff" stroke="#f26a10" stroke-width="4"/><path d="M19 14v20l15-10z" fill="#f26a10"/></svg>
</section>

<!-- features -->
<div class="abs feature center" style="left:143px;top:2772px;background:var(--blue)">
  <h3>Reducing Industrial<br>Impacts</h3>
  <p>Lorem ipsum dolor sit amet, cctetur adipisicing elit, sed do eiusmod tempor incididunt ut labore et dolore magna aliqua. Ut enim ad minim veniam, quis nostrud exetion ullamco laboris nisi ut aliquip ex ea commodo consequat.</p>
</div>
<div class="abs feature center" style="left:458px;top:2772px;background:var(--orange)">
  <h3>Working Together</h3>
  <p>Lorem ipsum dolor sit amet, cctetur adipisicing elit, sed do eiusmod tempor incididunt ut labore et dolore magna aliqua. Ut enim ad minim veniam, quis nostrud exetion ullamco laboris nisi ut aliquip ex ea commodo consequat.</p>
</div>
<div class="abs feature center" style="left:773px;top:2772px;background:var(--blue)">
  <h3>Monitoring Populations</h3>
  <p>Lorem ipsum dolor sit amet, cctetur adipisicing elit, sed do eiusmod tempor incididunt ut labore et dolore magna aliqua. Ut enim ad minim veniam, quis nostrud exetion ullamco laboris nisi ut aliquip ex ea commodo consequat.</p>
</div>
<svg class="abs" style="left:250px;top:2746px" width="68" height="68"><rect width="68" height="68" fill="#fff"/><path d="M8 58V36l12-8v8l12-8v8l12-8V12h8v46Z" fill="none" stroke="#22b5e2" stroke-width="2.5"/><rect x="14" y="44" width="6" height="6" fill="none" stroke="#22b5e2" stroke-width="2"/><rect x="26" y="44" width="6" height="6" fill="none" stroke="#22b5e2" stroke-width="2"/><rect x="38" y="44" width="6" height="6" fill="none" stroke="#22b5e2" stroke-width="2"/></svg>
<svg class="abs" style="left:565px;top:2746px" width="68" height="68"><rect width="68" height="68" fill="#fff"/><circle cx="34" cy="26" r="14" fill="none" stroke="#f26a10" stroke-width="2.5"/><circle cx="34" cy="26" r="5" fill="none" stroke="#f26a10" stroke-width="2.5"/><path d="M20 58c2-10 26-10 28 0" fill="none" stroke="#f26a10" stroke-width="2.5"/></svg>
<svg class="abs" style="left:880px;top:2746px" width="68" height="68"><rect width="68" height="68" fill="#fff"/><rect x="10" y="14" width="48" height="32" fill="none" stroke="#f26a10" stroke-width="2.5"/><path d="M34 46v8M24 56h20" stroke="#f26a10" stroke-width="2.5"/><path d="M16 40l10-10 8 6 14-14" fill="none" stroke="#f26a10" stroke-width="2.5"/></svg>

<!-- news -->
<section class="abs news" role="img" aria-label="Dark-toned photo of a smiling group of volunteers">
  <svg class="abs" style="left:0;top:0" width="1200" height="853">
    <path d="M0 0H1200Q600 134 0 0Z" fill="#fff"/>
    <path d="M0 853V820Q600 720 1200 790V853Z" fill="#f2f2f2"/>
  </svg>
</section>
<h2 class="abs news center" style="top:3320px;height:auto;background:none">LATEST NEWS</h2>
<div class="abs" style="left:570px;top:3384px;width:60px;height:4px;background:#fff"></div>

<div class="abs card center" style="left:147px;top:3442px">
  <div class="photo" role="img" aria-label="Photo of a group of volunteers holding donation bags" style="background:linear-gradient(180deg,#9aa58a,#5d6a58)"><div class="date">Oct<br>2020</div></div>
  <h4>Sed ut perspiciatis unde<br>omnis iste natus</h4>
  <p>Sed ut perspiciatis unde omnis iste natus error sit voluptatem accutium doloque laium, totam rem</p>
  <div class="more">READ MORE</div>
</div>
<div class="abs card center" style="left:458px;top:3442px">
  <div class="photo" role="img" aria-label="Photo of a polar bear swimming underwater" style="background:linear-gradient(180deg,#3aa7c9,#1a6f8d)"><div class="date">Oct<br>2020</div></div>
  <h4>Sed ut perspiciatis unde<br>omnis iste natus</h4>
  <p>Sed ut perspiciatis unde omnis iste natus error sit voluptatem accutium doloque laium, totam rem</p>
  <div class="more">READ MORE</div>
</div>
<div class="abs card center" style="left:771px;top:3442px">
  <div class="photo" role="img" aria-label="Photo of cupped hands holding a red heart" style="background:radial-gradient(circle at 50% 50%,#d6262a,#c98f74 45%,#e4d5cc)"><div class="date">Oct<br>2020</div></div>
  <h4>Sed ut perspiciatis unde<br>omnis iste natus</h4>
  <p>Sed ut perspiciatis unde omnis iste natus error sit voluptatem accutium doloque laium, totam rem</p>
  <div class="more">READ MORE</div>
</div>

<!-- gift -->
<section class="abs gift">
  <div class="abs brand-name" style="left:0;width:1200px;justify-content:center;top:72px;font-size:36px"><span class="dot" style="width:28px;height:28px"></span>Marlowe Bright Works</div>
  <h2 class="abs center" style="top:152px">Donate $100 and Receive A Free<br>3 Night Vacation Certificate To Las Vegas!</h2>
  <p class="abs center" style="top:241px">Lorem ipsum dolor sit amet, consectetur adipiscing elit, sed do eiusmod tempor</p>
  <div class="btn-pill" style="left:431px;top:289px;width:338px;font-size:14px">
    <span class="heart"><svg width="14" height="13" viewBox="0 0 24 22"><path d="M12 21 2 11A6 6 0 0 1 12 3a6 6 0 0 1 10 8Z" fill="#f26a10"/></svg></span>Incentive Gift for the Donation
  </div>
</section>

<!-- footer -->
<footer class="abs footer">
  <div class="abs brand-name" style="left:147px;top:70px;font-size:26px"><span class="dot"></span>Marlowe Bright Works</div>
  <div class="abs foot-item" style="left:147px;top:168px;width:300px">
    <svg width="16" height="20" viewBox="0 0 16 20"><path d="M8 19C3 12 1 9 1 7a7 7 0 0 1 14 0c0 2-2 5-7 12Z" fill="none" stroke="#ddd" stroke-width="1.6"/><circle cx="8" cy="7" r="2.5" fill="none" stroke="#ddd" stroke-width="1.6"/></svg>
    <div>4417 Larkspur Way<br>Fenwick County, ON, Canada</div>
  </div>
  <div class="abs foot-item" style="left:147px;top:226px;width:300px">
    <svg width="16" height="16" viewBox="0 0 16 16"><path d="M3 1l3 3-2 2c1 2 3 4 5 5l2-2 3 3-2 3C7 15 1 9 1 3Z" fill="none" stroke="#ddd" stroke-width="1.6"/></svg>
    <div>Phone :<br>555-0142-7788</div>
  </div>
  <div class="abs foot-item" style="left:147px;top:284px;width:320px">
    <svg width="18" height="14" viewBox="0 0 18 14"><rect x="1" y="1" width="16" height="12" fill="none" stroke="#ddd" stroke-width="1.6"/><path d="M1 1l8 7 8-7" fill="none" stroke="#ddd" stroke-width="1.6"/></svg>
    <div>Email :<br>hello@marlowe-bright-works.example</div>
  </div>

  <h5 class="abs" style="left:496px;top:62px">Sign Up To Receive Email</h5>
  <p class="abs" style="left:496px;top:108px;width:330px;font-size:13px;line-height:21px">Excepteur sint occaecat cupidatat non proident, sunt in culpa qui Nemo enim ipsam voluptatem</p>
  <div class="abs email-field" style="left:496px;top:174px">Enter Email</div>
  <div class="btn-box" style="left:496px;top:230px;width:120px;height:38px;background:var(--blue);font-size:14px">Subscribe</div>

  <h5 class="abs" style="left:878px;top:62px">Quick Links</h5>
  <div class="abs quick" style="left:882px;top:104px">
    <a>Home</a><a>About</a><a>Services</a><a>Donate Now</a><a>Blog</a><a>Contact</a>
  </div>
</footer>
<div class="abs copyright center">Copyright © Marlowe Bright Works 2020. All rights reserved. | Privacy Policy</div>

</body>
</html>
```